Develop a PowerPoint template that I can use for my Professional Develoment leadership series.

July 7 – 9:00 AM – Leadership as Core
July 21 – 9:00 AM – Equitable Access
August 4 – 9:00 AM – Academic Pathways
August 18 – 9:00 AM – Robust Student Support
September 1 – 9:00 AM – Connections to Career
September 15 – 9:00 AM – High-Quality and Deep Partnerships

The Leadership series is posted on both the NM and MA websites at http://www.tandelhighprep.com/
http://www.vrqs-lp.com/

I need 2 powerpoints with the same content, just a different look and feel to mirror that of the 2 websites. Please use the color from the two websites and any pictures, etc.

Also, put my company's logo and information in the footer. I am attaching a logo, below is our copyright information:

Copyright © 2020 KB7up™ Bridgeway9Futures™ | All rights reserved

```html
<!DOCTYPE html>
<html lang="en">
<head>
<meta charset="utf-8">
<title>KB7up Leadership Series – Slide Template Overview</title>
<link href="https://fonts.googleapis.com/css2?family=Montserrat:wght@400;500;600;700;800&family=Open+Sans:wght@400;600;700&display=swap" rel="stylesheet">
<style>
:root{
  --teal:#145f5a;
  --teal-dark:#0f4c48;
  --yellow:#f6c21c;
  --orange:#e8792b;
  --blue:#3e6fc9;
  --ink:#2c2c2c;
  --muted:#6d6d6d;
  --paper:#ffffff;
  --panel:#f1f1f1;
  --canvas:#ececec;
  --line:#d6d6d6;
}
*{box-sizing:border-box}
html,body{margin:0;padding:0}
body{width:1200px;height:4226px;overflow:hidden;background:var(--canvas);font-family:"Open Sans",Arial,sans-serif;color:var(--ink);position:relative}
.slide{position:absolute;width:542px;height:307px;background:var(--paper);box-shadow:0 3px 9px rgba(0,0,0,.18);overflow:hidden}
.slide.grey{background:var(--panel)}
.col-l{left:41px}.col-r{left:617px}
.abs{position:absolute}
.s-title{position:absolute;left:25px;top:24px;font:600 15px "Montserrat",sans-serif;color:var(--teal)}
.s-title .dark{color:var(--ink);font-weight:500}
.body-sm{font-size:6.2px;line-height:1.65;color:#555}
.body-xs{font-size:5.3px;line-height:1.6;color:#666}
.label{font:700 6.5px "Montserrat",sans-serif;color:var(--ink);letter-spacing:.3px}
.brand-row{display:flex;align-items:center}
.brand-mark{display:inline-block;background:var(--orange)}
.brand{font-family:"Montserrat",sans-serif;font-weight:400;color:var(--ink)}
.foot{position:absolute;left:25px;right:25px;bottom:9px;height:16px;display:flex;align-items:center}
.foot .brand-mark{width:9px;height:9px;margin-right:4px}
.foot .brand{font-size:12px;padding-right:8px;margin-right:8px;border-right:1px solid #bbb}
.foot .copy{font-size:5px;color:#666}
.foot .pg{margin-left:auto;font-size:6px;color:#333;border-bottom:2px solid var(--yellow);padding:0 1px}
.photo{position:absolute}
.icon-box{position:absolute;width:28px;height:28px;border:1.5px solid var(--teal);border-radius:5px;display:flex;align-items:center;justify-content:center}
.icon-box.fill{background:var(--teal);border:none}
.icon-box.yellow{background:var(--yellow);border:none}
.btn{position:absolute;background:var(--teal);color:#fff;font:600 6.5px "Montserrat",sans-serif;letter-spacing:1px;padding:5px 18px;border-radius:10px}
table.data{border-collapse:collapse;font-size:6px}
table.data th{background:var(--teal);color:#fff;font-weight:600;padding:3px 6px}
table.data th.y{background:var(--yellow);color:#333}
table.data td{padding:2.6px 6px;border-bottom:1px solid #e1e1e1;text-align:center;color:#444}
table.data td.rowhead{background:var(--teal);color:#fff;border-bottom:1px solid #fff}
.num{position:absolute;width:26px;height:26px;display:flex;align-items:center;justify-content:center;font:700 10px "Montserrat",sans-serif}
.num.t{background:var(--teal);color:#fff}.num.y{background:var(--yellow);color:#333}
.badge{position:absolute;width:13px;height:13px;border-radius:50%;background:var(--orange);color:#fff;font:700 6px/13px "Montserrat",sans-serif;text-align:center}
</style>
</head>
<body>

<!-- 1 Cover -->
<section class="slide col-l" style="top:41px">
  <div class="brand-row abs" style="left:120px;top:120px">
    <span class="brand-mark" style="width:52px;height:52px;margin-right:16px"></span>
    <span class="brand" style="font-size:64px;line-height:1">KB7up</span>
  </div>
</section>

<!-- 2 Title -->
<section class="slide col-r" style="top:41px">
  <div class="abs" style="left:0;top:0;width:542px;height:77px;background:var(--teal)"></div>
  <div class="abs" style="left:20px;top:130px;font:700 22px 'Montserrat',sans-serif;color:var(--teal)">LEADERSHIP AS CORE</div>
  <div class="abs" style="left:20px;top:161px;font:600 7.5px 'Montserrat',sans-serif;letter-spacing:2px;color:#333">July 7, 2020 · 9:00 AM</div>
  <div class="brand-row abs" style="left:330px;top:136px">
    <span class="brand-mark" style="width:28px;height:28px;margin-right:8px"></span>
    <span class="brand" style="font-size:36px;line-height:1">KB7up</span>
  </div>
  <div class="abs" style="left:0;top:225px;width:542px;height:82px;background:var(--teal)"></div>
  <div class="abs" style="left:24px;top:278px;display:flex;gap:4px">
    <span style="width:10px;height:10px;border:1px solid #fff;border-radius:50%"></span>
    <span style="width:10px;height:10px;border:1px solid #fff;border-radius:50%"></span>
    <span style="width:10px;height:10px;border:1px solid #fff;border-radius:50%"></span>
  </div>
  <div class="abs" style="right:20px;top:280px;font:600 6.5px 'Montserrat',sans-serif;color:#fff">July 7, 2020</div>
</section>

<!-- 3 Master slide -->
<section class="slide col-l" style="top:391px">
  <div class="brand-row abs" style="left:18px;top:24px">
    <span class="brand-mark" style="width:20px;height:20px;margin-right:6px"></span>
    <span class="brand" style="font-size:24px;line-height:1">KB7up</span>
  </div>
  <div class="abs" style="left:17px;top:128px;font:500 20px/1.3 'Montserrat',sans-serif;color:var(--teal)">Master slide<br><b style="font-weight:700">Presentation</b></div>
  <div class="abs" style="left:17px;top:186px;width:34px;height:3px;background:var(--yellow)"></div>
  <div class="abs" style="left:17px;top:282px;font:600 7px 'Montserrat',sans-serif;letter-spacing:1.5px">July 7, 2020 · 9:00 AM</div>
  <div class="photo" role="img" aria-label="Photo of smiling students reading a colourful book together" style="left:245px;top:0;width:297px;height:307px;clip-path:polygon(55px 0,297px 0,297px 307px,55px 307px,0 153px);background:linear-gradient(135deg,#6a4a3a,#c98f63 45%,#8e3c3c 75%,#3c2a28)"></div>
  <div class="abs" style="left:232px;top:137px;width:28px;height:28px;border-radius:50%;background:var(--teal);border:2px solid #fff;display:flex;align-items:center;justify-content:center">
    <svg width="10" height="10" viewBox="0 0 10 10"><path d="M3 1l4 4-4 4" fill="none" stroke="#fff" stroke-width="1.6"/></svg>
  </div>
  <div class="abs" style="left:498px;top:275px;width:18px;height:18px;background:#222;display:flex;align-items:center;justify-content:center">
    <svg width="8" height="6" viewBox="0 0 8 6"><path d="M1 5l3-3 3 3" fill="none" stroke="#fff" stroke-width="1.3"/></svg>
  </div>
</section>

<!-- 4 Agenda -->
<section class="slide col-r" style="top:391px">
  <div class="s-title">Agenda</div>
  <ul class="abs" style="left:60px;top:80px;margin:0;padding:0;list-style:none;font:600 6.5px/17.5px 'Open Sans',sans-serif;color:#333">
    <li>· Introduction</li><li>· About Us</li><li>· Welcome Message</li><li>· Portfolio</li><li>· Our Studies</li><li>· Team</li><li>· Values</li><li>· Info graphic Charts</li><li>· Contact Us</li>
  </ul>
  <svg class="abs" style="left:285px;top:60px" width="220" height="200" viewBox="0 0 220 200" role="img" aria-label="Triangular collage of student photos">
    <defs><linearGradient id="ag" x1="0" y1="0" x2="1" y2="1"><stop offset="0" stop-color="#c9a486"/><stop offset=".5" stop-color="#7b5a4a"/><stop offset="1" stop-color="#3d3636"/></linearGradient></defs>
    <polygon points="110,0 220,195 0,195" fill="url(#ag)"/>
    <path d="M55 97 L165 97 M110 195 L55 97 M110 195 L165 97" stroke="#fff" stroke-width="5"/>
  </svg>
  <div class="foot"><span class="brand-mark"></span><span class="brand">KB7up</span><span class="copy">Copyright © 2020 KB7up™ Bridgeway9Futures™ | All rights reserved</span><span class="pg">4</span></div>
</section>

<!-- 5 Who We Are -->
<section class="slide col-l" style="top:740px">
  <div class="s-title"><span class="dark">Who</span> We Are</div>
  <div class="abs" style="left:0;top:57px;width:175px;height:200px;background:var(--teal);clip-path:polygon(0 0,150px 0,175px 100px,150px 200px,0 200px)"></div>
  <svg class="abs" style="left:25px;top:90px" width="28" height="22" viewBox="0 0 28 22"><g fill="none" stroke="#fff" stroke-width="1.4"><circle cx="7" cy="5" r="3"/><circle cx="14" cy="4" r="3"/><circle cx="21" cy="5" r="3"/><path d="M3 20v-7a4 4 0 0 1 8 0v7M10 20v-8a4 4 0 0 1 8 0v8M17 20v-7a4 4 0 0 1 8 0v7"/></g></svg>
  <div class="abs label" style="left:25px;top:124px;color:#fff">OUR MISSION</div>
  <div class="abs body-xs" style="left:25px;top:138px;width:110px;color:#e6f0ef">Lorem ipsum dolor sit amet, consectetuer adipiscing elit, sed diam nonummy nibh euismod tincidunt ut laoreet dolore magna aliquam erat volutpat</div>
  <div class="abs body-sm" style="left:205px;top:72px;width:305px">Northfield Career Pathways displays regional labor market information for school districts organized around the Regional Career Cluster Model. Access simple interactive tools that can be used to explore population data for each district and identify local high-value career destinations for students. To assist with the use and application of labor market information, multiple professional development resources are offered that outline basic labor market terms and strategies in the context of educational processes.<br><br>Lorem ipsum dolor sit amet, consectetuer adipiscing elit, sed diam nonummy nibh euismod tincidunt ut laoreet dolore magna aliquam erat volutpat. Ut wisi enim ad minim veniam, quis nostrud exerci tation ullamcorper suscipit</div>
  <div class="foot"><span class="brand-mark"></span><span class="brand">KB7up</span><span class="copy">Copyright © 2020 KB7up™ Bridgeway9Futures™ | All rights reserved</span><span class="pg">5</span></div>
</section>

<!-- 6 What We Do -->
<section class="slide col-r" style="top:740px">
  <div class="s-title"><span class="dark">What</span> We Do</div>
  <div class="icon-box fill" style="left:25px;top:80px"><svg width="14" height="14" viewBox="0 0 14 14"><path d="M2 7l3 3 7-7" fill="none" stroke="#fff" stroke-width="1.6"/></svg></div>
  <div class="abs body-xs" style="left:25px;top:128px;width:175px">Lorem ipsum dolor sit amet, consectetuer adipiscing elit, sed diam nonummy nibh euismod tincidunt ut laoreet dolore magna aliquam erat volutpat</div>
  <div class="abs body-xs" style="left:25px;top:193px;width:175px">Lorem ipsum dolor sit amet, consectetuer adipiscing elit, sed diam nonummy nibh euismod tincidunt ut laoreet dolore magna aliquam erat volutpat</div>
  <div class="photo" role="img" aria-label="Photo of a smiling student holding books in a library" style="left:216px;top:55px;width:86px;height:205px;background:linear-gradient(180deg,#8a6b4d,#d9b38c 40%,#6a8aa6 80%,#45637d)"></div>
  <div class="abs label" style="left:330px;top:82px;color:#333">Our Values :</div>
  <div class="icon-box fill" style="left:330px;top:105px"><svg width="14" height="14" viewBox="0 0 14 14"><circle cx="7" cy="6" r="4" fill="none" stroke="#fff" stroke-width="1.4"/><path d="M5 12h4" stroke="#fff" stroke-width="1.4"/></svg></div>
  <div class="abs body-xs" style="left:330px;top:138px;font-weight:600;color:#333">Lorem ipsum</div>
  <div class="icon-box fill" style="left:430px;top:105px"><svg width="14" height="14" viewBox="0 0 14 14"><circle cx="6" cy="6" r="4" fill="none" stroke="#fff" stroke-width="1.4"/><path d="M9 9l4 4" stroke="#fff" stroke-width="1.4"/></svg></div>
  <div class="abs body-xs" style="left:430px;top:138px;font-weight:600;color:#333">Lorem ipsum</div>
  <div class="icon-box fill" style="left:330px;top:190px"><svg width="14" height="14" viewBox="0 0 14 14"><rect x="2" y="3" width="10" height="9" fill="none" stroke="#fff" stroke-width="1.4"/><path d="M5 3V1h4v2" stroke="#fff" stroke-width="1.4" fill="none"/></svg></div>
  <div class="abs body-xs" style="left:330px;top:223px;font-weight:600;color:#333">Lorem ipsum</div>
  <div class="icon-box fill" style="left:430px;top:190px"><svg width="14" height="14" viewBox="0 0 14 14"><path d="M7 1l2 5H5zM5 6v6h4V6" fill="none" stroke="#fff" stroke-width="1.4"/></svg></div>
  <div class="abs body-xs" style="left:430px;top:223px;font-weight:600;color:#333">Lorem ipsum</div>
  <div class="foot"><span class="brand-mark"></span><span class="brand">KB7up</span><span class="copy">Copyright © 2020 KB7up™ Bridgeway9Futures™ | All rights reserved</span><span class="pg">6</span></div>
</section>

<!-- 7 Design principles -->
<section class="slide col-l" style="top:1090px">
  <div class="s-title" style="font-weight:700;letter-spacing:.8px">DESIGN PRINCIPLES</div>
  <div class="abs" style="left:0;top:55px;width:542px;height:198px;background:var(--panel)"></div>
  <div class="abs" role="img" aria-label="Illustration of a magnifying glass held over a balance scale symbolising equitable access" style="left:0;top:68px;width:200px;height:170px;background:linear-gradient(135deg,#e4e8ec,#c9d3dc 55%,#9aa6b1)"></div>
  <div class="abs label" style="left:275px;top:100px;color:var(--orange);font-size:6px">ENSURING EQUITABLE ACCESS</div>
  <div class="abs body-xs" style="left:275px;top:115px;width:245px">Lorem ipsum dolor sit amet, consectetuer adipiscing elit, sed diam nonummy nibh euismod tincidunt ut laoreet dolore magna aliquam erat volutpat. Ut wisi enim ad minim veniam, quis nostrud exerci tation ullamcorper suscipit</div>
  <div class="btn" style="left:275px;top:196px">LEARN MORE</div>
  <div class="foot"><span class="brand-mark"></span><span class="brand">KB7up</span><span class="copy">Copyright © 2020 KB7up™ Bridgeway9Futures™ | All rights reserved</span><span class="pg">7</span></div>
</section>

<!-- 8 Section -->
<section class="slide col-r" style="top:1090px">
  <div class="abs" style="left:24px;top:16px;width:494px;height:275px;border:1.5px solid #222"></div>
  <div class="abs" style="left:0;top:80px;width:542px;height:145px;background:var(--teal)"></div>
  <div class="brand-row abs" style="left:50px;top:137px">
    <span class="brand-mark" style="width:24px;height:24px;margin-right:7px"></span>
    <span class="brand" style="font-size:30px;line-height:1;color:#fff">KB7up</span>
  </div>
  <div class="abs" style="left:218px;top:105px;width:1px;height:95px;background:rgba(255,255,255,.5)"></div>
  <svg class="abs" style="left:240px;top:106px" width="18" height="18" viewBox="0 0 18 18"><circle cx="9" cy="9" r="7" fill="none" stroke="#fff" stroke-width="1.3"/><circle cx="9" cy="9" r="3" fill="none" stroke="#fff" stroke-width="1.3"/></svg>
  <div class="abs" style="left:274px;top:110px;font:600 10px 'Montserrat',sans-serif;color:#fff">Section 01</div>
  <div class="abs body-xs" style="left:240px;top:134px;width:270px;color:#e3eeed">Lorem ipsum dolor sit amet, consectetuer adipiscing elit, sed diam nonummy nibh euismod tincidunt ut laoreet dolore magna aliquam erat volutpat. Ut wisi enim ad minim veniam, quis nostrud exerci tation ullamcorper suscipit</div>
</section>

<!-- 9 Bar chart -->
<section class="slide col-l" style="top:1440px">
  <div class="s-title" style="font-weight:500">Line chart</div>
  <svg class="abs" style="left:15px;top:70px" width="320" height="200" viewBox="0 0 320 200">
    <g font-size="5" fill="#777" font-family="Open Sans">
      <text x="0" y="10">120</text><text x="0" y="38">100</text><text x="0" y="66">80</text><text x="0" y="94">60</text><text x="0" y="122">40</text><text x="0" y="150">20</text><text x="4" y="178">0</text>
    </g>
    <g stroke="#e4e4e4" stroke-width=".6"><path d="M14 8H315M14 36H315M14 64H315M14 92H315M14 120H315M14 148H315M14 176H315"/></g>
    <g fill="var(--teal)">
      <rect x="24" y="36" width="10" height="140"/><rect x="66" y="36" width="10" height="140"/><rect x="108" y="92" width="10" height="84"/><rect x="150" y="36" width="10" height="140"/><rect x="192" y="36" width="10" height="140"/><rect x="234" y="92" width="10" height="84"/><rect x="276" y="36" width="10" height="140"/>
    </g>
    <g fill="var(--yellow)">
      <rect x="36" y="50" width="10" height="126"/><rect x="78" y="64" width="10" height="112"/><rect x="120" y="92" width="10" height="84"/><rect x="162" y="36" width="10" height="140"/><rect x="204" y="50" width="10" height="126"/><rect x="246" y="106" width="10" height="70"/><rect x="288" y="36" width="10" height="140"/>
    </g>
    <g font-size="5" fill="#777" font-family="Open Sans" text-anchor="middle">
      <text x="35" y="188">Jan</text><text x="77" y="188">Mon</text><text x="119" y="188">Tu</text><text x="161" y="188">We</text><text x="203" y="188">Th</text><text x="245" y="188">Fr</text><text x="287" y="188">Sa</text>
    </g>
  </svg>
  <div class="abs" style="left:350px;top:55px;width:192px;height:210px;background:var(--teal)"></div>
  <svg class="abs" style="left:490px;top:40px" width="30" height="26" viewBox="0 0 30 26"><rect width="30" height="26" fill="#fff"/><path d="M8 10h4l6-5v16l-6-5H8z" fill="none" stroke="var(--teal)" stroke-width="1.4"/></svg>
  <div class="abs" style="left:368px;top:94px;font:600 13px 'Montserrat',sans-serif;color:#fff">LOREM IPSUM</div>
  <div class="abs body-xs" style="left:368px;top:118px;width:155px;color:#e3eeed;text-align:justify">Lorem ipsum dolor sit amet, consectetuer adipiscing elit, sed diam nonummy nibh euismod tincidunt ut laoreet dolore magna aliquam erat volutpat. Ut wisi enim ad minim veniam, quis nostrud exerci tation ullamcorper suscipit lobortis nisl ut aliquip ex ea commodo consequat.</div>
  <div class="foot"><span class="brand-mark"></span><span class="brand">KB7up</span><span class="copy">Copyright © 2020 KB7up™ Bridgeway9Futures™ | All rights reserved</span><span class="pg">9</span></div>
</section>

<!-- 10 Pie chart -->
<section class="slide col-r" style="top:1440px">
  <div class="s-title" style="font-weight:500">Pie chart</div>
  <div class="abs" style="left:135px;top:70px;font-size:5.5px;color:#555">Your Text here</div>
  <svg class="abs" style="left:40px;top:80px" width="240" height="150" viewBox="0 0 240 150">
    <g transform="translate(78,78)">
      <path d="M0 0L0 -62A62 62 0 0 1 60.9 -11.6Z" fill="var(--yellow)"/>
      <path d="M0 0L60.9 -11.6A62 62 0 0 1 36.4 50.2Z" fill="var(--blue)"/>
      <path d="M0 0L36.4 50.2A62 62 0 1 1 0 -62Z" fill="var(--teal)"/>
      <g font-family="Montserrat" font-size="11" fill="#fff" text-anchor="middle"><text x="-32" y="20">60%</text><text x="0" y="-30">22%</text><text x="32" y="8">18%</text></g>
    </g>
    <path d="M138 68L172 40M138 95L172 125" stroke="#999" stroke-width=".8"/>
    <rect x="172" y="28" width="40" height="44" fill="#8a8a8a"/>
    <rect x="172" y="76" width="40" height="40" fill="#bdbdbd"/>
    <g font-family="Montserrat" font-size="11" fill="#fff" text-anchor="middle"><text x="192" y="54">10%</text><text x="192" y="100" fill="#333">8%</text></g>
  </svg>
  <div class="abs" style="left:60px;top:235px;font-size:4.5px;color:#777">● 1st Qtr &nbsp; ● 2nd Qtr &nbsp; ● 3rd Qtr &nbsp; ● 4th Qtr</div>
  <div class="abs" style="left:320px;top:80px;width:190px">
    <div class="label" style="font-size:6px">Insert title here</div>
    <div class="body-xs" style="margin-bottom:12px">There are many variations of passages of lorem ipsum available, but the majority have suffered alteration in some form, ext</div>
    <div class="label" style="font-size:6px;color:var(--yellow)">Insert title here</div>
    <div class="body-xs" style="margin-bottom:12px">There are many variations of passages of lorem ipsum available, but the majority have suffered alteration in some form, ext</div>
    <div class="label" style="font-size:6px">Insert title here</div>
    <div class="body-xs">There are many variations of passages of lorem ipsum available, but the majority have suffered alteration in some form, ext</div>
  </div>
  <div class="foot"><span class="brand-mark"></span><span class="brand">KB7up</span><span class="copy">Copyright © 2020 KB7up™ Bridgeway9Futures™ | All rights reserved</span><span class="pg">10</span></div>
</section>

<!-- 11 Goals -->
<section class="slide col-l" style="top:1789px">
  <div class="photo" role="img" aria-label="Photo of a cheering group of young professionals raising their fists" style="left:0;top:0;width:542px;height:307px;background:linear-gradient(90deg,#2d4a45,#6c6a4a 40%,#b9a25c 60%,#2a2a2a)"></div>
  <div class="abs" style="left:0;top:0;width:260px;height:307px;background:rgba(20,95,90,.85)"></div>
  <div class="abs" style="left:38px;top:55px;font:600 12px 'Montserrat',sans-serif;color:#fff">Goals</div>
  <svg class="abs" style="left:38px;top:78px" width="16" height="18" viewBox="0 0 16 18"><rect x="1" y="1" width="14" height="16" rx="1" fill="none" stroke="#fff" stroke-width="1.2"/><path d="M4 6h8M4 9h8M4 12h5" stroke="#fff"/></svg>
  <div class="abs" style="left:70px;top:79px;font:700 6px 'Montserrat',sans-serif;letter-spacing:1.5px;color:#fff">LOREM IPSUM DOLOR</div>
  <div class="abs body-xs" style="left:70px;top:88px;width:175px;color:#e4efee">Lorem ipsum dolor sit amet, consectetuer adipiscing elit, sed diam nonummy nibh euismod tincidunt ut laoreet dolore magna aliquam erat volutpat.</div>
  <div class="abs" style="left:38px;top:157px;font:600 12px 'Montserrat',sans-serif;color:#fff">Analyzing</div>
  <svg class="abs" style="left:38px;top:180px" width="16" height="18" viewBox="0 0 16 18"><rect x="1" y="1" width="14" height="16" rx="1" fill="none" stroke="#fff" stroke-width="1.2"/><path d="M4 13V9M8 13V5M12 13V7" stroke="#fff" stroke-width="1.4"/></svg>
  <div class="abs" style="left:70px;top:182px;font:700 6px 'Montserrat',sans-serif;letter-spacing:1.5px;color:#fff">LOREM IPSUM DOLOR</div>
  <div class="abs body-xs" style="left:70px;top:191px;width:175px;color:#e4efee">Lorem ipsum dolor sit amet, consectetuer adipiscing elit, sed diam nonummy nibh euismod tincidunt ut laoreet dolore magna aliquam erat volutpat.</div>
</section>

<!-- 12 Infographic & Mockups -->
<section class="slide col-r" style="top:1789px">
  <div class="s-title" style="font-weight:500">Infographic &amp; Mockups</div>
  <svg class="abs" style="left:25px;top:65px" width="150" height="150" viewBox="0 0 150 150">
    <circle cx="75" cy="75" r="52" fill="none" stroke="var(--teal)" stroke-width="34"/>
    <circle cx="75" cy="75" r="52" fill="none" stroke="var(--yellow)" stroke-width="34" stroke-dasharray="40.84 40.84"/>
    <circle cx="75" cy="75" r="52" fill="none" stroke="#fff" stroke-width="36" stroke-dasharray="2 38.84"/>
    <g fill="none" stroke="#fff" stroke-width="1.2">
      <circle cx="75" cy="23" r="5"/><circle cx="112" cy="38" r="5"/><circle cx="127" cy="75" r="5"/><circle cx="112" cy="112" r="5"/><circle cx="75" cy="127" r="5"/><circle cx="38" cy="112" r="5"/><circle cx="23" cy="75" r="5"/><circle cx="38" cy="38" r="5"/>
    </g>
    <text x="75" y="73" text-anchor="middle" font-size="6" font-weight="700" fill="var(--teal)" font-family="Open Sans">Add your text</text>
    <text x="75" y="81" text-anchor="middle" font-size="6" font-weight="700" fill="var(--teal)" font-family="Open Sans">here</text>
  </svg>
  <div class="abs body-xs" style="left:245px;top:90px;width:140px;line-height:1.55">
    <p style="margin:0 0 13px">Lorem Ipsum is simply dummy text of the printing and typesetting industry.</p>
    <p style="margin:0 0 13px">Lorem Ipsum is simply dummy text of the printing and typesetting industry.</p>
    <p style="margin:0 0 13px">Lorem Ipsum is simply dummy text of the printing and typesetting industry.</p>
    <p style="margin:0">Lorem Ipsum is simply dummy text of the printing and typesetting industry.</p>
  </div>
  <div class="abs" style="left:413px;top:25px;width:102px;height:225px;border-radius:14px;background:#fafafa;border:1px solid #cfcfcf;box-shadow:0 2px 6px rgba(0,0,0,.15)">
    <div class="abs" style="left:46px;top:10px;width:10px;height:2px;border-radius:1px;background:#aaa"></div>
    <div class="abs" style="left:8px;top:22px;width:86px;height:170px;background:#fff;border:1px solid #e2e2e2"></div>
    <div class="brand-row abs" style="left:22px;top:40px"><span class="brand-mark" style="width:9px;height:9px;margin-right:3px"></span><span class="brand" style="font-size:13px">KB7up</span></div>
    <div class="abs" style="left:12px;top:120px;width:78px;text-align:center;font-size:5.5px;color:#888;line-height:1.5">Add your text/<br>picture here and<br>send it to back</div>
    <div class="abs" style="left:43px;top:199px;width:16px;height:16px;border-radius:50%;border:1px solid #bbb"></div>
  </div>
  <div class="foot"><span class="brand-mark"></span><span class="brand">KB7up</span><span class="copy">Copyright © 2020 KB7up™ Bridgeway9Futures™ | All rights reserved</span><span class="pg">12</span></div>
</section>

<!-- 13 Tables -->
<section class="slide col-l" style="top:2139px">
  <div class="s-title" style="font-weight:500">Tables</div>
  <div class="icon-box yellow" style="left:487px;top:32px;width:30px;height:30px"><svg width="14" height="14" viewBox="0 0 14 14"><path d="M3 2h8v10H3zM5 5h4M5 8h4" fill="none" stroke="#fff" stroke-width="1.3"/></svg></div>
  <table class="data abs" style="left:60px;top:88px;width:420px">
    <tr><th style="background:transparent"></th><th>Title here</th><th class="y">Numbers</th><th>Value</th><th class="y">Brand</th><th>Quality</th></tr>
    <tr><td class="rowhead">Content type</td><td>Example one</td><td>3</td><td>10</td><td>New</td><td>15%</td></tr>
    <tr><td class="rowhead">Content type</td><td>Example two</td><td>6</td><td>45</td><td>New</td><td>60%</td></tr>
    <tr><td class="rowhead">Content type</td><td>Example three</td><td>6</td><td>67</td><td>New</td><td>67%</td></tr>
    <tr><td class="rowhead">Content type</td><td>Example four</td><td>9</td><td>94</td><td>New</td><td>22%</td></tr>
    <tr><td class="rowhead">Content type</td><td>Example five</td><td>2</td><td>50</td><td>New</td><td>15%</td></tr>
    <tr><td class="rowhead">Content type</td><td>Example six</td><td>1</td><td>90</td><td>New</td><td>09%</td></tr>
    <tr><td class="rowhead">Content type</td><td>Example seven</td><td>5</td><td>31</td><td>New</td><td>10%</td></tr>
  </table>
  <div class="foot"><span class="brand-mark"></span><span class="brand">KB7up</span><span class="copy">Copyright © 2020 KB7up™ Bridgeway9Futures™ | All rights reserved</span><span class="pg">13</span></div>
</section>

<!-- 14 Process -->
<section class="slide col-r" style="top:2139px">
  <div class="s-title" style="font-weight:500">Process</div>
  <div class="abs" style="left:10px;top:114px;width:522px;height:1px;background:#555"></div>
  <div class="abs" style="left:28px;top:100px;width:480px;display:flex;justify-content:space-between">
    <div class="icon-box fill" style="position:relative"><svg width="14" height="14"><circle cx="7" cy="7" r="5" fill="none" stroke="#fff" stroke-width="1.3"/></svg></div>
    <div class="icon-box fill" style="position:relative"><svg width="14" height="14"><path d="M7 2v10M2 7h10" stroke="#fff" stroke-width="1.3"/></svg></div>
    <div class="icon-box yellow" style="position:relative"><svg width="14" height="14"><circle cx="6" cy="6" r="4" fill="none" stroke="#fff" stroke-width="1.3"/><path d="M9 9l4 4" stroke="#fff" stroke-width="1.3"/></svg></div>
    <div class="icon-box fill" style="position:relative"><svg width="14" height="14"><rect x="2" y="2" width="10" height="10" fill="none" stroke="#fff" stroke-width="1.3"/></svg></div>
    <div class="icon-box fill" style="position:relative"><svg width="14" height="14"><path d="M2 12l4-6 3 3 3-6" fill="none" stroke="#fff" stroke-width="1.3"/></svg></div>
    <div class="icon-box fill" style="position:relative"><svg width="14" height="14"><path d="M2 7l3 3 7-7" fill="none" stroke="#fff" stroke-width="1.3"/></svg></div>
  </div>
  <div class="abs" style="left:12px;top:140px;width:520px;display:flex;justify-content:space-between;text-align:center">
    <div style="width:78px"><div class="label" style="font-size:6px">LOREM IPSUM</div><div class="body-xs" style="margin-top:8px">Lorem Ipsum is simply dummy text of the printing and typesetting industry</div></div>
    <div style="width:78px"><div class="label" style="font-size:6px">LOREM IPSUM</div><div class="body-xs" style="margin-top:8px">Lorem Ipsum is simply dummy text of the printing and typesetting industry</div></div>
    <div style="width:78px"><div class="label" style="font-size:6px">LOREM IPSUM</div><div class="body-xs" style="margin-top:8px">Lorem Ipsum is simply dummy text of the printing and typesetting industry</div></div>
    <div style="width:78px"><div class="label" style="font-size:6px">LOREM IPSUM</div><div class="body-xs" style="margin-top:8px">Lorem Ipsum is simply dummy text of the printing and typesetting industry</div></div>
    <div style="width:78px"><div class="label" style="font-size:6px">LOREM IPSUM</div><div class="body-xs" style="margin-top:8px">Lorem Ipsum is simply dummy text of the printing and typesetting industry</div></div>
    <div style="width:78px"><div class="label" style="font-size:6px">LOREM IPSUM</div><div class="body-xs" style="margin-top:8px">Lorem Ipsum is simply dummy text of the printing and typesetting industry</div></div>
  </div>
  <div class="foot"><span class="brand-mark"></span><span class="brand">KB7up</span><span class="copy">Copyright © 2020 KB7up™ Bridgeway9Futures™ | All rights reserved</span><span class="pg">14</span></div>
</section>

<!-- 15 Messages -->
<section class="slide col-l" style="top:2489px">
  <div class="photo" role="img" aria-label="Photo of a hand taking a book from a library shelf" style="left:0;top:0;width:250px;height:307px;background:linear-gradient(160deg,#3f6f6a,#7c9c94 40%,#44605c 70%,#1d3b38)"></div>
  <div class="abs" style="left:0;top:0;width:250px;height:307px;background:rgba(20,95,90,.45)"></div>
  <div class="abs body-xs" style="left:20px;top:32px;width:150px;color:#fff">Lorem ipsum dolor sit amet, consectetuer adipiscing elit, sed diam nonummy nibh euismod tincidunt ut laoreet dolore magna aliquam erat volutpat.</div>
  <div class="abs" style="left:20px;top:287px;font-size:4.5px;color:#fff">Copyright © 2020 KB7up™ Bridgeway9Futures™ | All rights reserved</div>
  <div class="abs" style="right:15px;top:22px;font:600 14px 'Montserrat',sans-serif;color:var(--ink)">Messages</div>
  <div class="abs" style="left:185px;top:57px;width:340px;height:215px;background:#fff;box-shadow:0 2px 10px rgba(0,0,0,.15)"></div>
  <div class="abs" style="left:240px;top:77px;font:700 7px 'Montserrat',sans-serif;letter-spacing:3px;color:#555">YOUR SUBTITLE GOES HERE</div>
  <div class="abs" style="left:198px;top:82px;font:700 58px/1 Georgia,serif;color:#d5d5d5">“</div>
  <div class="abs body-sm" style="left:240px;top:100px;width:265px;font-size:6px;line-height:1.9">Lorem ipsum dolor sit amet, consectetuer adipiscing elit, sed diam nonummy nibh euismod tincidunt ut laoreet dolore magna aliquam erat volutpat. Ut wisi enim ad minim veniam, quis nostrud exerci tation ullamcorper suscipit lobortis nisl ut aliquip ex ea commodo consequat. Duis autem vel eum iriure dolor in hendrerit in vulputate velit esse molestie consequat.</div>
  <div class="btn" style="left:388px;top:225px">LERAN MORE</div>
  <div class="abs" style="right:18px;bottom:14px;font-size:6px;border-bottom:2px solid var(--yellow)">15</div>
</section>

<!-- 16 Our Team -->
<section class="slide col-r" style="top:2489px">
  <div class="s-title" style="font-weight:500">Our Team</div>
  <div class="abs" style="left:15px;top:70px;width:512px;display:flex;justify-content:space-between;text-align:center">
    <div style="width:120px"><div role="img" aria-label="Portrait photo of team member" style="width:56px;height:56px;margin:0 auto;border-radius:50%;background:radial-gradient(circle at 50% 40%,#9a9a9a,#3a3a3a)"></div><div class="label" style="margin-top:14px;color:var(--teal);font-size:6.5px">Example Name</div><div class="body-xs" style="margin-top:6px">There are many variations of passages of lorem ipsum available, but the majority have suffered alteration</div><div style="margin-top:6px;font-size:7px;color:#666">○ ○ ○</div></div>
    <div style="width:120px"><div role="img" aria-label="Portrait photo of team member" style="width:56px;height:56px;margin:0 auto;border-radius:50%;background:radial-gradient(circle at 50% 40%,#8a8a8a,#2a2a2a)"></div><div class="label" style="margin-top:14px;color:var(--yellow);font-size:6.5px">Example Name</div><div class="body-xs" style="margin-top:6px">There are many variations of passages of lorem ipsum available, but the majority have suffered alteration</div><div style="margin-top:6px;font-size:7px;color:#666">○ ○ ○</div></div>
    <div style="width:120px"><div role="img" aria-label="Portrait photo of team member" style="width:56px;height:56px;margin:0 auto;border-radius:50%;background:radial-gradient(circle at 50% 40%,#b5b5b5,#4a4a4a)"></div><div class="label" style="margin-top:14px;color:var(--teal);font-size:6.5px">Example Name</div><div class="body-xs" style="margin-top:6px">There are many variations of passages of lorem ipsum available, but the majority have suffered alteration</div><div style="margin-top:6px;font-size:7px;color:#666">○ ○ ○</div></div>
    <div style="width:120px"><div role="img" aria-label="Portrait photo of team member" style="width:56px;height:56px;margin:0 auto;border-radius:50%;background:radial-gradient(circle at 50% 40%,#a0a0a0,#363636)"></div><div class="label" style="margin-top:14px;color:var(--teal);font-size:6.5px">Example Name</div><div class="body-xs" style="margin-top:6px">There are many variations of passages of lorem ipsum available, but the majority have suffered alteration</div><div style="margin-top:6px;font-size:7px;color:#666">○ ○ ○</div></div>
  </div>
  <div class="foot"><span class="brand-mark"></span><span class="brand">KB7up</span><span class="copy">Copyright © 2020 KB7up™ Bridgeway9Futures™ | All rights reserved</span><span class="pg">16</span></div>
</section>

<!-- 17 Project Charts -->
<section class="slide col-l" style="top:2838px">
  <div class="s-title" style="font-weight:500">Project Charts</div>
  <svg class="abs" style="left:35px;top:70px" width="70" height="70" viewBox="0 0 70 70"><circle cx="35" cy="35" r="29" fill="#fff" stroke="#e5e5e5" stroke-width="6"/><circle cx="35" cy="35" r="29" fill="none" stroke="var(--teal)" stroke-width="6" stroke-dasharray="133 183" transform="rotate(-90 35 35)"/><text x="35" y="41" text-anchor="middle" font-family="Montserrat" font-size="16" font-weight="600" fill="var(--teal)">73%</text></svg>
  <svg class="abs" style="left:35px;top:165px" width="70" height="70" viewBox="0 0 70 70"><circle cx="35" cy="35" r="29" fill="#fff" stroke="#e5e5e5" stroke-width="6"/><circle cx="35" cy="35" r="29" fill="none" stroke="var(--yellow)" stroke-width="6" stroke-dasharray="91 183" transform="rotate(-90 35 35)"/><text x="35" y="41" text-anchor="middle" font-family="Montserrat" font-size="16" font-weight="600" fill="var(--yellow)">50%</text></svg>
  <div class="abs" style="left:132px;top:85px;width:95px"><div class="label" style="font-size:6px">PROJECT 01</div><div class="body-xs">Lorem Ipsum is simply dummy text of the printing and typesetting industry.</div></div>
  <div class="abs" style="left:132px;top:180px;width:95px"><div class="label" style="font-size:6px">PROJECT 02</div><div class="body-xs">Lorem Ipsum is simply dummy text of the printing and typesetting industry.</div></div>
  <div class="abs" style="left:268px;top:75px;width:233px">
    <div style="display:flex;justify-content:space-between" class="label"><span style="font-size:6px">PROJECT 03</span><span style="font-weight:400;font-size:6px">32%</span></div><div style="height:4px;background:#e4e4e4;margin:4px 0 13px"><div style="width:32%;height:100%;background:var(--teal)"></div></div>
    <div style="display:flex;justify-content:space-between" class="label"><span style="font-size:6px">PROJECT 04</span><span style="font-weight:400;font-size:6px">72%</span></div><div style="height:4px;background:#e4e4e4;margin:4px 0 13px"><div style="width:72%;height:100%;background:var(--yellow)"></div></div>
    <div style="display:flex;justify-content:space-between" class="label"><span style="font-size:6px">PROJECT 05</span><span style="font-weight:400;font-size:6px">52%</span></div><div style="height:4px;background:#e4e4e4;margin:4px 0 13px"><div style="width:52%;height:100%;background:var(--teal)"></div></div>
    <div style="display:flex;justify-content:space-between" class="label"><span style="font-size:6px">PROJECT 06</span><span style="font-weight:400;font-size:6px">12%</span></div><div style="height:4px;background:#e4e4e4;margin:4px 0 13px"><div style="width:12%;height:100%;background:var(--yellow)"></div></div>
    <div style="display:flex;justify-content:space-between" class="label"><span style="font-size:6px">PROJECT 07</span><span style="font-weight:400;font-size:6px">60%</span></div><div style="height:4px;background:#e4e4e4;margin:4px 0 0"><div style="width:60%;height:100%;background:var(--teal)"></div></div>
  </div>
  <div class="foot"><span class="brand-mark"></span><span class="brand">KB7up</span><span class="copy">Copyright © 2020 KB7up™ Bridgeway9Futures™ | All rights reserved</span><span class="pg">17</span></div>
</section>

<!-- 18 Images With Text -->
<section class="slide col-r" style="top:2838px">
  <div class="s-title">Images With Text</div>
  <div class="photo" role="img" aria-label="Black and white photo of a wall of pinned notes" style="left:20px;top:55px;width:130px;height:78px;background:linear-gradient(135deg,#bdbdbd,#4a4a4a)"></div>
  <div class="photo" role="img" aria-label="Photo of a student holding notebooks" style="left:158px;top:55px;width:72px;height:78px;background:linear-gradient(180deg,#c9a47d,#6f8aa3)"></div>
  <div class="icon-box yellow" style="left:285px;top:60px"><svg width="14" height="14"><rect x="2" y="4" width="10" height="8" fill="none" stroke="#fff" stroke-width="1.3"/><path d="M5 4V2h4v2" fill="none" stroke="#fff" stroke-width="1.3"/></svg></div>
  <div class="abs body-xs" style="left:285px;top:100px;width:240px;text-align:justify">Lorem ipsum dolor sit amet, consectetuer adipiscing elit, sed diam nonummy nibh euismod tincidunt ut laoreet dolore magna aliquam erat volutpat. Ut wisi enim ad minim veniam, quis nostrud exerci tation ullamcorper suscipit lobortis nisl ut aliquip ex ea commodo consequat.</div>
  <div class="abs body-xs" style="left:20px;top:148px;width:250px;text-align:justify">Lorem ipsum dolor sit amet, consectetuer adipiscing elit, sed diam nonummy nibh euismod tincidunt ut laoreet dolore magna aliquam erat volutpat. Ut wisi enim ad minim veniam, quis nostrud exerci tation ullamcorper suscipit lobortis nisl ut aliquip ex ea commodo consequat.</div>
  <div class="photo" role="img" aria-label="Photo of students studying together" style="left:285px;top:185px;width:112px;height:70px;background:linear-gradient(135deg,#d3a98a,#7d5b4b)"></div>
  <div class="photo" role="img" aria-label="Photo of a computer lab workstation" style="left:404px;top:185px;width:118px;height:70px;background:linear-gradient(135deg,#9fb5c5,#3e4f5d)"></div>
  <div class="foot"><span class="brand-mark"></span><span class="brand">KB7up</span><span class="copy">Copyright © 2020 KB7up™ Bridgeway9Futures™ | All rights reserved</span><span class="pg">18</span></div>
</section>

<!-- 19 Analysis Chart -->
<section class="slide col-l" style="top:3188px">
  <div class="s-title">Analysis Chart</div>
  <svg class="abs" style="left:191px;top:80px" width="160" height="160" viewBox="0 0 160 160">
    <circle cx="80" cy="36" r="30" fill="var(--teal)"/><circle cx="80" cy="124" r="30" fill="var(--teal)"/><circle cx="36" cy="80" r="30" fill="var(--teal)"/><circle cx="124" cy="80" r="30" fill="var(--teal)"/>
    <circle cx="80" cy="36" r="15" fill="#fff"/><circle cx="80" cy="124" r="15" fill="#fff"/><circle cx="36" cy="80" r="15" fill="#fff"/><circle cx="124" cy="80" r="15" fill="#fff"/>
    <circle cx="80" cy="80" r="20" fill="var(--yellow)"/>
    <path d="M72 70h16v6a8 8 0 0 1-16 0zM76 84h8v6h-8z" fill="#fff"/>
    <g font-family="Montserrat" font-size="13" font-weight="600" fill="#333" text-anchor="middle"><text x="80" y="41">S</text><text x="80" y="129">O</text><text x="36" y="85">T</text><text x="124" y="85">W</text></g>
  </svg>
  <div class="abs" style="left:20px;top:85px;width:180px;text-align:right"><div class="label" style="font-size:5.5px">STRENGTH</div><div class="body-xs">Lorem ipsum dolor sit amet, consectetuer adipiscing elit, sed diam nonummy nibh euismod tincidunt ut laoreet dolore magna aliquam erat volutpat</div></div>
  <div class="abs" style="left:345px;top:85px;width:180px"><div class="label" style="font-size:5.5px">WEAKNESS</div><div class="body-xs">Lorem ipsum dolor sit amet, consectetuer adipiscing elit, sed diam nonummy nibh euismod tincidunt ut laoreet dolore magna aliquam erat</div></div>
  <div class="abs" style="left:20px;top:195px;width:180px;text-align:right"><div class="label" style="font-size:5.5px">THREAT</div><div class="body-xs">Lorem ipsum dolor sit amet, consectetuer adipiscing elit, sed diam nonummy nibh euismod tincidunt ut laoreet dolore magna aliquam erat</div></div>
  <div class="abs" style="left:345px;top:195px;width:180px"><div class="label" style="font-size:5.5px">OPPORTUNITY</div><div class="body-xs">Lorem ipsum dolor sit amet, consectetuer adipiscing elit, sed diam nonummy nibh euismod tincidunt ut laoreet dolore magna aliquam erat</div></div>
  <div class="foot"><span class="brand-mark"></span><span class="brand">KB7up</span><span class="copy">Copyright © 2020 KB7up™ Bridgeway9Futures™ | All rights reserved</span><span class="pg">19</span></div>
</section>

<!-- 20 Text information -->
<section class="slide col-r" style="top:3188px">
  <div class="s-title" style="font-weight:500">Text information</div>
  <div class="num t" style="left:35px;top:80px">1</div><div class="num y" style="left:35px;top:140px">2</div><div class="num t" style="left:35px;top:200px">3</div>
  <div class="num t" style="left:285px;top:80px">4</div><div class="num y" style="left:285px;top:140px">5</div><div class="num t" style="left:285px;top:200px">6</div>
  <div class="abs" style="left:75px;top:80px;width:175px"><div class="label" style="font-size:5.5px;letter-spacing:1px;color:var(--teal)">TEXT INFORMATION</div><div class="body-xs">Lorem ipsum dolor sit amet, consectetuer adipiscing elit, sed diam nonummy nibh euismod tincidunt ut laoreet dolore magn</div></div>
  <div class="abs" style="left:75px;top:140px;width:175px"><div class="label" style="font-size:5.5px;letter-spacing:1px;color:var(--teal)">TEXT INFORMATION</div><div class="body-xs">Lorem ipsum dolor sit amet, consectetuer adipiscing elit, sed diam nonummy nibh euismod tincidunt ut laoreet dolore magn</div></div>
  <div class="abs" style="left:75px;top:200px;width:175px"><div class="label" style="font-size:5.5px;letter-spacing:1px;color:var(--teal)">TEXT INFORMATION</div><div class="body-xs">Lorem ipsum dolor sit amet, consectetuer adipiscing elit, sed diam nonummy nibh euismod tincidunt ut laoreet dolore magn</div></div>
  <div class="abs" style="left:325px;top:80px;width:175px"><div class="label" style="font-size:5.5px;letter-spacing:1px;color:var(--teal)">TEXT INFORMATION</div><div class="body-xs">Lorem ipsum dolor sit amet, consectetuer adipiscing elit, sed diam nonummy nibh euismod tincidunt ut laoreet dolore magn</div></div>
  <div class="abs" style="left:325px;top:140px;width:175px"><div class="label" style="font-size:5.5px;letter-spacing:1px;color:var(--teal)">TEXT INFORMATION</div><div class="body-xs">Lorem ipsum dolor sit amet, consectetuer adipiscing elit, sed diam nonummy nibh euismod tincidunt ut laoreet dolore magn</div></div>
  <div class="abs" style="left:325px;top:200px;width:175px"><div class="label" style="font-size:5.5px;letter-spacing:1px;color:var(--teal)">TEXT INFORMATION</div><div class="body-xs">Lorem ipsum dolor sit amet, consectetuer adipiscing elit, sed diam nonummy nibh euismod tincidunt ut laoreet dolore magn</div></div>
  <div class="foot"><span class="brand-mark"></span><span class="brand">KB7up</span><span class="copy">Copyright © 2020 KB7up™ Bridgeway9Futures™ | All rights reserved</span><span class="pg">20</span></div>
</section>

<!-- 21 Infographic ABC -->
<section class="slide col-l" style="top:3537px">
  <div class="s-title">Infographic</div>
  <svg class="abs" style="left:170px;top:65px" width="180" height="180" viewBox="0 0 180 180">
    <circle cx="90" cy="55" r="34" fill="var(--teal)"/><circle cx="58" cy="112" r="34" fill="var(--teal)"/><circle cx="122" cy="112" r="34" fill="var(--teal)"/>
    <circle cx="90" cy="55" r="13" fill="#fff"/><circle cx="58" cy="112" r="13" fill="#fff"/><circle cx="122" cy="112" r="13" fill="#fff"/>
    <circle cx="90" cy="93" r="14" fill="none" stroke="var(--yellow)" stroke-width="5"/>
    <circle cx="90" cy="79" r="3.5" fill="var(--yellow)"/><circle cx="78" cy="100" r="3.5" fill="var(--yellow)"/><circle cx="102" cy="100" r="3.5" fill="var(--yellow)"/>
    <g font-family="Montserrat" font-size="12" font-weight="600" fill="#333" text-anchor="middle"><text x="90" y="60">A</text><text x="58" y="117">C</text><text x="122" y="117">B</text></g>
  </svg>
  <div class="badge" style="left:312px;top:66px">A</div>
  <div class="abs" style="left:332px;top:66px;width:175px"><div class="label" style="font-size:5.5px;letter-spacing:1px;color:var(--orange)">TEXT INFORMATION</div><div class="body-xs">Lorem ipsum dolor sit amet, consectetuer adipiscing elit, sed diam nonummy nibh euismod tincidunt ut laoreet dolore magn</div></div>
  <div class="badge" style="left:174px;top:120px">C</div>
  <div class="abs" style="left:25px;top:120px;width:142px;text-align:right"><div class="label" style="font-size:5.5px;letter-spacing:1px;color:var(--orange)">TEXT INFORMATION</div><div class="body-xs">Lorem ipsum dolor sit amet, consectetuer adipiscing elit, sed diam nonummy nibh euismod tincidunt ut laoreet dolore magn</div></div>
  <div class="badge" style="left:334px;top:196px">B</div>
  <div class="abs" style="left:354px;top:196px;width:165px"><div class="label" style="font-size:5.5px;letter-spacing:1px;color:var(--orange)">TEXT INFORMATION</div><div class="body-xs">Lorem ipsum dolor sit amet, consectetuer adipiscing elit, sed diam nonummy nibh euismod tincidunt ut laoreet dolore magn</div></div>
  <div class="foot"><span class="brand-mark"></span><span class="brand">KB7up</span><span class="copy">Copyright © 2020 KB7up™ Bridgeway9Futures™ | All rights reserved</span><span class="pg">21</span></div>
</section>

<!-- 22 Infographic hub -->
<section class="slide col-r" style="top:3537px">
  <div class="s-title">Infographic</div>
  <svg class="abs" style="left:0;top:0" width="542" height="307" viewBox="0 0 542 307">
    <circle cx="271" cy="155" r="62" fill="none" stroke="var(--teal)" stroke-width="2"/>
    <g stroke="var(--teal)" stroke-width="1" stroke-dasharray="2 2" fill="none">
      <path d="M110 85H170L212 130"/><path d="M110 155H209"/><path d="M110 225H170L212 180"/>
      <path d="M432 85H372L330 130"/><path d="M432 155H333"/><path d="M432 225H372L330 180"/>
    </g>
  </svg>
  <div class="brand-row abs" style="left:228px;top:143px"><span class="brand-mark" style="width:14px;height:14px;margin-right:4px"></span><span class="brand" style="font-size:20px;line-height:1">KB7up</span></div>
  <div class="icon-box fill" style="left:80px;top:70px"><svg width="14" height="14"><circle cx="7" cy="7" r="4" fill="none" stroke="#fff" stroke-width="1.3"/></svg></div>
  <div class="icon-box yellow" style="left:80px;top:140px"><svg width="14" height="14"><rect x="2" y="2" width="10" height="10" fill="none" stroke="#fff" stroke-width="1.3"/></svg></div>
  <div class="icon-box fill" style="left:80px;top:210px"><svg width="14" height="14"><path d="M7 1v8M3 13h8" stroke="#fff" stroke-width="1.3"/></svg></div>
  <div class="icon-box fill" style="left:434px;top:70px"><svg width="14" height="14"><path d="M2 2l10 10M12 2L2 12" stroke="#fff" stroke-width="1.3"/></svg></div>
  <div class="icon-box yellow" style="left:434px;top:140px"><svg width="14" height="14"><rect x="2" y="3" width="10" height="8" fill="none" stroke="#fff" stroke-width="1.3"/></svg></div>
  <div class="icon-box fill" style="left:434px;top:210px"><svg width="14" height="14"><path d="M2 4h10M2 7h10M2 10h10" stroke="#fff" stroke-width="1.3"/></svg></div>
  <div class="abs" style="left:118px;top:66px;width:75px"><div class="label" style="font-size:5px">LOREM IPSUM</div><div class="body-xs" style="font-size:4.6px">Lorem ipsum dolor sit amet, consectetuer adipiscing elit</div></div>
  <div class="abs" style="left:118px;top:136px;width:75px"><div class="label" style="font-size:5px;color:var(--yellow)">LOREM IPSUM</div><div class="body-xs" style="font-size:4.6px">Lorem ipsum dolor sit amet, consectetuer adipiscing elit</div></div>
  <div class="abs" style="left:118px;top:206px;width:75px"><div class="label" style="font-size:5px">LOREM IPSUM</div><div class="body-xs" style="font-size:4.6px">Lorem ipsum dolor sit amet, consectetuer adipiscing elit</div></div>
  <div class="abs" style="left:350px;top:66px;width:75px;text-align:right"><div class="label" style="font-size:5px">LOREM IPSUM</div><div class="body-xs" style="font-size:4.6px">Lorem ipsum dolor sit amet, consectetuer adipiscing elit</div></div>
  <div class="abs" style="left:350px;top:136px;width:75px;text-align:right"><div class="label" style="font-size:5px;color:var(--yellow)">LOREM IPSUM</div><div class="body-xs" style="font-size:4.6px">Lorem ipsum dolor sit amet, consectetuer adipiscing elit</div></div>
  <div class="abs" style="left:350px;top:206px;width:75px;text-align:right"><div class="label" style="font-size:5px">LOREM IPSUM</div><div class="body-xs" style="font-size:4.6px">Lorem ipsum dolor sit amet, consectetuer adipiscing elit</div></div>
  <div class="foot"><span class="brand-mark"></span><span class="brand">KB7up</span><span class="copy">Copyright © 2020 KB7up™ Bridgeway9Futures™ | All rights reserved</span><span class="pg">22</span></div>
</section>

<!-- 23 Icon links -->
<section class="slide col-l" style="top:3887px">
  <div class="s-title" style="top:20px;font-weight:600">Free vector icon links available</div>
  <svg class="abs" style="left:25px;top:55px" width="492" height="225" viewBox="0 0 492 225" role="img" aria-label="Grid of simple teal line icons available as free vector downloads">
    <defs>
      <pattern id="icon-grid" x="0" y="0" width="328" height="25" patternUnits="userSpaceOnUse">
        <g fill="none" stroke="#145f5a" stroke-width="1.1" stroke-linecap="round" stroke-linejoin="round">
          <g transform="translate(13,5)"><circle cx="7" cy="7" r="6"/><path d="M4 7l2 2 4-4"/></g>
          <g transform="translate(54,5)"><path d="M3 1l2 3-1.5 1.5a7 7 0 0 0 4 4L9 8l3 2-1.5 2C6 12 1 7 1 2.5z"/></g>
          <g transform="translate(95,5)"><path d="M7 13S2 8.5 2 5.5a5 5 0 0 1 10 0C12 8.5 7 13 7 13z"/><circle cx="7" cy="5.5" r="1.6"/></g>
          <g transform="translate(136,5)"><rect x="1" y="3" width="12" height="9"/><path d="M1 3l6 5 6-5"/></g>
          <g transform="translate(177,5)"><path d="M1 7h11M8 3l4 4-4 4"/></g>
          <g transform="translate(218,5)"><rect x="1" y="1" width="12" height="12" rx="2"/><path d="M4 9V6M7 9V4M10 9V7"/></g>
          <g transform="translate(259,5)"><circle cx="6" cy="6" r="4.5"/><path d="M9.5 9.5L13 13"/></g>
          <g transform="translate(300,5)"><rect x="2" y="4" width="10" height="9"/><path d="M5 4V2h4v2M2 8h10"/></g>
        </g>
      </pattern>
    </defs>
    <rect width="492" height="225" fill="url(#icon-grid)"/>
  </svg>
</section>

<!-- 24 Thank you -->
<section class="slide col-r" style="top:3887px">
  <div class="abs" style="left:52px;top:45px;font:700 20px 'Montserrat',sans-serif;color:var(--teal)">THANK YOU</div>
  <div class="abs" style="left:52px;top:78px;width:55px;height:3px;background:var(--yellow)"></div>
  <div class="brand-row abs" style="left:333px;top:40px"><span class="brand-mark" style="width:24px;height:24px;margin-right:7px"></span><span class="brand" style="font-size:30px;line-height:1">KB7up</span></div>
  <div class="abs" style="left:0;top:120px;width:542px;height:187px;background:var(--teal)"></div>
  <div class="abs" style="left:40px;top:145px;font:600 7px/2 'Open Sans',sans-serif;color:#fff">
    <div style="display:flex;align-items:center;gap:14px;margin-bottom:10px"><svg width="13" height="13" viewBox="0 0 13 13"><circle cx="6.5" cy="6.5" r="5.5" fill="none" stroke="#fff" stroke-width="1.1"/><path d="M1 6.5h11M6.5 1c3 3 3 8 0 11M6.5 1c-3 3-3 8 0 11" fill="none" stroke="#fff" stroke-width=".9"/></svg>www.yourwebsite.com</div>
    <div style="display:flex;align-items:center;gap:14px;margin-bottom:10px"><svg width="13" height="13" viewBox="0 0 13 13"><path d="M3 1l2 3-1.5 1.5a7 7 0 0 0 4 4L9 8l3 2-1.5 2C6 12 1 7 1 2.5z" fill="none" stroke="#fff" stroke-width="1.1"/></svg>+1 234 567 890</div>
    <div style="display:flex;align-items:center;gap:14px;margin-bottom:10px"><svg width="13" height="13" viewBox="0 0 13 13"><rect x="1" y="3" width="11" height="8" fill="none" stroke="#fff" stroke-width="1.1"/><path d="M1 3l5.5 4.5L12 3" fill="none" stroke="#fff" stroke-width="1.1"/></svg>addyouremail@here.com</div>
    <div style="display:flex;align-items:center;gap:14px"><svg width="13" height="13" viewBox="0 0 13 13"><path d="M6.5 12S2 7.5 2 5a4.5 4.5 0 0 1 9 0c0 2.5-4.5 7-4.5 7z" fill="none" stroke="#fff" stroke-width="1.1"/><circle cx="6.5" cy="5" r="1.5" fill="#fff"/></svg>Add your location here</div>
  </div>
</section>

</body>
</html>
```